Poster Design for kebab shop products

need a new poster for our new velmo pack special, sign will be inside of shopping centre at different location to shop will need to stand out and draw customers to the store, MUST contain shops logo & picture added, poster size will be 76cm x 101cm so will need to suit that size

MUST ALSO CONTAIN THE FOLLOWING
Velmo Pack / HSP
Lamb & Chips
Chicken & Chips
Beef & Chips
+ Can $15

Target Market(s)

new customers

Industry/Entity Type

Retail

Font styles to use
Sans Serif

Colors

Designer to choose colors to be used in the design.

Requirements
Must have
• company logo
• picture of vemo pack provided
• Velmo Pack / HSP
• Lamb & Chips
• Chicken & Chips
• Beef & Chips
• + Can $15

```html
<!DOCTYPE html>
<html lang="en">
<head>
<meta charset="utf-8">
<title>Skewer Cove – Velmo Pack Special Poster</title>
<link rel="stylesheet" href="https://fonts.googleapis.com/css2?family=Lobster&family=Open+Sans:wght@700;800&family=Montserrat:wght@900&display=swap">
<style>
  :root {
    --orange-light: #fbb55a;
    --orange: #f3901e;
    --red: #ee1c25;
    --ink: #2b2b2b;
    --white: #ffffff;
    --tray: #f1f1ef;
    --tray-shade: #d9d9d6;
    --silver-light: #f2f2f2;
    --silver: #c9c9c9;
    --brand-red: #c8181e;
  }
  html, body {
    margin: 0;
    padding: 0;
    width: 872px;
    height: 1200px;
    overflow: hidden;
    background: var(--white);
  }
  .poster {
    position: relative;
    width: 872px;
    height: 1200px;
    overflow: hidden;
    font-family: "Open Sans", Arial, sans-serif;
  }
  .poster__shapes {
    position: absolute;
    inset: 0;
  }
  .headline {
    position: absolute;
    left: 0;
    width: 872px;
    top: 592px;
    text-align: center;
    margin: 0;
    font-family: "Lobster", cursive;
    font-weight: 400;
    font-size: 80px;
    line-height: 1;
    color: var(--ink);
    text-shadow: 2px 2px 0 var(--white), -1px -1px 0 var(--white), 1px -1px 0 var(--white), -1px 1px 0 var(--white);
  }
  .menu-list {
    position: absolute;
    left: 108px;
    top: 762px;
    margin: 0;
    padding: 0;
    list-style: none;
  }
  .menu-list__item {
    display: flex;
    align-items: center;
    height: 45px;
    font-weight: 700;
    font-size: 28px;
    color: var(--white);
  }
  .menu-list__tick {
    width: 16px;
    height: 16px;
    margin-right: 18px;
    flex: none;
  }
  .price {
    position: absolute;
    left: 478px;
    top: 755px;
    margin: 0;
    font-family: "Montserrat", Arial, sans-serif;
    font-weight: 900;
    font-size: 150px;
    line-height: 1;
    letter-spacing: -4px;
    color: var(--ink);
    text-shadow: 2px 2px 0 var(--white);
  }
  .brand {
    position: absolute;
    left: 0;
    width: 872px;
    top: 1075px;
    display: flex;
    justify-content: center;
    align-items: center;
    gap: 14px;
  }
  .brand__dot {
    width: 40px;
    height: 40px;
    border-radius: 50%;
    background: var(--orange);
  }
  .brand__name {
    font-weight: 800;
    font-size: 36px;
    color: var(--brand-red);
  }
</style>
</head>
<body>
<main class="poster">
  <svg class="poster__shapes" width="872" height="1200" viewBox="0 0 872 1200">
    <defs>
      <radialGradient id="burst" cx="0.5" cy="0.35" r="0.75">
        <stop offset="0" stop-color="var(--orange-light)"/>
        <stop offset="1" stop-color="var(--orange)"/>
      </radialGradient>
      <linearGradient id="silver" x1="0" y1="0" x2="1" y2="0">
        <stop offset="0" stop-color="var(--silver)"/>
        <stop offset="0.5" stop-color="var(--silver-light)"/>
        <stop offset="1" stop-color="var(--silver)"/>
      </linearGradient>
      <linearGradient id="food" x1="0" y1="0" x2="1" y2="1">
        <stop offset="0" stop-color="#8a5a34"/>
        <stop offset="0.45" stop-color="#c98a4a"/>
        <stop offset="1" stop-color="#f2d36a"/>
      </linearGradient>
    </defs>

    <!-- orange header backdrop -->
    <rect class="header-backdrop" x="0" y="0" width="872" height="420" fill="url(#burst)"/>

    <!-- red body -->
    <path class="body-red" d="M0,336 Q460,300 872,385 L872,1200 L0,1200 Z" fill="var(--red)"/>

    <!-- takeaway tray -->
    <path class="tray" d="M78,70 L790,70 Q808,70 806,90 L792,480 Q790,498 772,498 L486,498 L478,576 L401,576 L393,498 L104,498 Q86,498 84,480 L62,90 Q60,70 78,70 Z"
          fill="var(--tray)" stroke="var(--tray-shade)" stroke-width="3"/>

    <!-- product photo area -->
    <rect class="product-photo" x="131" y="88" width="620" height="396" rx="30"
          fill="url(#food)" role="img" aria-label="Photo of a Velmo Pack: sliced kebab meat over chips with garlic and chilli sauce in a foam tray"/>

    <!-- swoosh under headline -->
    <path class="swoosh" d="M156,720 Q460,680 766,702 L763,738 Q470,694 156,722 Z" fill="var(--ink)" stroke="var(--white)" stroke-width="2"/>

    <!-- divider -->
    <rect class="divider" x="445" y="755" width="2" height="175" fill="var(--white)"/>

    <!-- footer -->
    <path class="footer-band" d="M0,1060 Q436,960 872,1066 L872,1200 L0,1200 Z" fill="var(--ink)"/>
    <path class="footer-silver" d="M0,1078 Q436,980 872,1084 L872,1200 L0,1200 Z" fill="url(#silver)"/>
  </svg>

  <h1 class="headline">Skewer Cove</h1>

  <ul class="menu-list">
    <li class="menu-list__item">
      <svg class="menu-list__tick" viewBox="0 0 16 16"><rect x="1" y="1" width="14" height="14" fill="none" stroke="#fff" stroke-width="1.5"/><path d="M4,8 L7,11 L12,4" fill="none" stroke="#fff" stroke-width="2"/></svg>
      Velmo Pack / HSP
    </li>
    <li class="menu-list__item">
      <svg class="menu-list__tick" viewBox="0 0 16 16"><rect x="1" y="1" width="14" height="14" fill="none" stroke="#fff" stroke-width="1.5"/><path d="M4,8 L7,11 L12,4" fill="none" stroke="#fff" stroke-width="2"/></svg>
      Lamb &amp; Chips
    </li>
    <li class="menu-list__item">
      <svg class="menu-list__tick" viewBox="0 0 16 16"><rect x="1" y="1" width="14" height="14" fill="none" stroke="#fff" stroke-width="1.5"/><path d="M4,8 L7,11 L12,4" fill="none" stroke="#fff" stroke-width="2"/></svg>
      Chicken &amp; Chips
    </li>
    <li class="menu-list__item">
      <svg class="menu-list__tick" viewBox="0 0 16 16"><rect x="1" y="1" width="14" height="14" fill="none" stroke="#fff" stroke-width="1.5"/><path d="M4,8 L7,11 L12,4" fill="none" stroke="#fff" stroke-width="2"/></svg>
      Beef &amp; Chips
    </li>
  </ul>

  <p class="price">$15</p>

  <div class="brand">
    <span class="brand__dot"></span>
    <span class="brand__name">Skewer Cove</span>
  </div>
</main>
</body>
</html>
```